Author needs a new book, Kindle and Audiobook cover design

I updated and re-edited a book I wrote 25 years ago but now realize the title and design did not get the job done. I am seeking a book, Kindle and audiobook design that will make me stand out. The final design will pop while being sensitive to the nature of the subject. The title of the book is Quiet Lanterns. Subtitle: Ways to Notice and Step Away From Harmful Circles While Keeping Steady Belief by Dorian T. Wexcombe. I am wanting to get the attention of people who have been damaged by a church relationship that started well but ended badly.
Updates

The book title is: Quiet Lanterns. The Subtitle is: Ways To Notice and Step Away From Harmful Circles While Keeping Steady Belief. The dimension is 6x9 (150 pages) and I am the author: Dorian T. Wexcombe

Target Market(s)

People with a church experience; church leadership. Religious abuse victims.

Industry/Entity Type

Christian

Font styles to use
Serif

Colors

Designer to choose colors to be used in the design.

Requirements
Nice to have
• I am not married to the Serif font if another design works better.

```html
<!DOCTYPE html>
<html lang="en">
<head>
<meta charset="utf-8">
<title>Quiet Lanterns — Dorian T. Wexcombe</title>
<link rel="stylesheet" href="https://fonts.googleapis.com/css2?family=Playfair+Display:wght@500;600&family=Open+Sans:wght@500&display=swap">
<style>
  :root {
    --ivy-deep: #0b1208;
    --ivy-dark: #17240f;
    --ivy-mid: #34491c;
    --window-glow: #f2c66e;
    --window-warm: #b98a3c;
    --title-cream: #f6e3ae;
    --subtitle-white: #f4f1e8;
    --author-cream: #f3e6c4;
  }
  html, body {
    margin: 0;
    padding: 0;
    width: 800px;
    height: 1200px;
    overflow: hidden;
    background: var(--ivy-deep);
  }
  .cover {
    position: relative;
    width: 800px;
    height: 1200px;
    overflow: hidden;
  }
  .cover-art {
    position: absolute;
    inset: 0;
    background:
      radial-gradient(ellipse 210px 330px at 440px 560px, var(--window-glow) 0%, var(--window-warm) 35%, rgba(60,70,25,0.6) 70%, transparent 100%),
      radial-gradient(ellipse 380px 520px at 420px 600px, var(--ivy-mid) 0%, var(--ivy-dark) 55%, var(--ivy-deep) 100%);
  }
  .title {
    position: absolute;
    top: 82px;
    left: 0;
    width: 800px;
    margin: 0;
    text-align: center;
    font-family: "Playfair Display", Georgia, serif;
    font-weight: 600;
    font-size: 122px;
    line-height: 104px;
    letter-spacing: 2px;
    text-transform: uppercase;
    color: var(--title-cream);
    text-shadow: 0 2px 10px rgba(0,0,0,0.45);
  }
  .title span { display: block; }
  .subtitle {
    position: absolute;
    top: 364px;
    left: 0;
    width: 800px;
    margin: 0;
    text-align: center;
    font-family: "Open Sans", Arial, sans-serif;
    font-weight: 500;
    font-size: 19px;
    line-height: 28px;
    letter-spacing: 0.5px;
    text-transform: uppercase;
    color: var(--subtitle-white);
  }
  .subtitle span {
    display: inline-block;
    padding: 0 8px;
    background: rgba(20,22,14,0.35);
  }
  .author {
    position: absolute;
    bottom: 44px;
    left: 0;
    width: 800px;
    margin: 0;
    text-align: center;
    font-family: "Playfair Display", Georgia, serif;
    font-weight: 500;
    font-size: 40px;
    letter-spacing: 9px;
    text-transform: uppercase;
    color: var(--author-cream);
  }
</style>
</head>
<body>
  <main class="cover">
    <div class="cover-art" role="img" aria-label="Photograph of an old cross-paned window glowing with warm light, framed by dense dark green ivy"></div>
    <h1 class="title"><span>Quiet</span><span>Lanterns</span></h1>
    <p class="subtitle"><span>Ways to Notice and Step Away From</span><br><span>Harmful Circles While Keeping Steady Belief</span></p>
    <p class="author">Dorian T. Wexcombe</p>
  </main>
</body>
</html>
```